Business Card Design Project

Need a business card that stands my education platform as a whole but

Target Market(s)

Parents, families, expats in the middle east.

Industry/Entity Type

Education

Contact Information for Business Card

www.brightsprout.ae
www.thehomenest.ae
www.thecarecirclehub.ae

+971543192704
rebecca@brightsprout.ae

Font styles to use
Serif

Requirements
Must have
• Logo's and contact details

```html
<!DOCTYPE html>
<html lang="en">
<head>
<meta charset="utf-8">
<title>Bright Sprout – Business Card</title>
<link rel="stylesheet" href="https://fonts.googleapis.com/css2?family=Fira+Sans:wght@400;600&display=swap">
<style>
  :root {
    --backdrop: #d9d9d9;
    --card: #ffffff;
    --teal: #2f7f94;
    --teal-badge: #3f8ea6;
    --orange: #f5914a;
    --shadow: rgba(0, 0, 0, 0.18);
  }
  * { box-sizing: border-box; margin: 0; padding: 0; }
  html, body {
    width: 1200px;
    height: 1079px;
    overflow: hidden;
    background: var(--backdrop);
    font-family: "Fira Sans", sans-serif;
  }
  .sheet {
    position: relative;
    width: 1200px;
    height: 1079px;
  }
  .card {
    position: absolute;
    left: 250px;
    width: 700px;
    height: 400px;
    background: var(--card);
    box-shadow: 0 8px 24px var(--shadow);
    overflow: hidden;
  }
  .card--front { top: 70px; }
  .card--back { top: 560px; }

  /* Front */
  .front-mark {
    position: absolute;
    inset: 0;
    display: flex;
    align-items: center;
    justify-content: center;
    gap: 18px;
  }
  .brand-dot {
    width: 34px;
    height: 34px;
    border-radius: 50%;
    background: var(--orange);
  }
  .brand-name {
    font-size: 52px;
    font-weight: 400;
    color: var(--teal);
    letter-spacing: 1px;
  }

  /* Back */
  .contact {
    position: absolute;
    left: 50px;
    top: 70px;
    display: grid;
    grid-template-columns: 78px auto;
    row-gap: 4px;
    column-gap: 14px;
    font-size: 22px;
    line-height: 30px;
  }
  .contact__label {
    color: var(--orange);
    font-weight: 600;
    text-align: right;
  }
  .contact__value { color: var(--teal); }
  .contact__value--stack { display: flex; flex-direction: column; }

  .back-logo {
    position: absolute;
    right: 40px;
    top: 70px;
    width: 200px;
    display: flex;
    flex-direction: column;
    align-items: center;
    gap: 18px;
  }
  .back-logo__name {
    display: flex;
    align-items: center;
    gap: 10px;
    font-size: 26px;
    color: var(--teal);
  }
  .back-logo__name .brand-dot { width: 18px; height: 18px; }
  .tagline {
    width: 190px;
    padding: 8px 10px;
    border-radius: 10px;
    background: var(--teal-badge);
    color: #ffffff;
    font-weight: 600;
    font-size: 16px;
    line-height: 20px;
    text-align: center;
  }
  .band {
    position: absolute;
    left: 0;
    right: 0;
    bottom: 0;
    height: 100px;
    background: var(--orange);
  }
</style>
</head>
<body>
<main class="sheet">
  <section class="card card--front" aria-label="Card front">
    <div class="front-mark">
      <span class="brand-dot"></span>
      <span class="brand-name">Bright Sprout</span>
    </div>
  </section>

  <section class="card card--back" aria-label="Card back">
    <div class="contact">
      <span class="contact__label">Web:</span>
      <span class="contact__value contact__value--stack">
        <span>www.brightsprout.ae</span>
        <span>www.thehomenest.ae</span>
        <span>www.thecarecirclehub.ae</span>
      </span>
      <span class="contact__label">Tell:</span>
      <span class="contact__value">+971543192704</span>
      <span class="contact__label">Email:</span>
      <span class="contact__value">rebecca@brightsprout.ae</span>
    </div>

    <div class="back-logo">
      <div class="back-logo__name">
        <span class="brand-dot"></span>
        <span>Bright Sprout</span>
      </div>
      <div class="tagline">Accelerated Learning Centre</div>
    </div>

    <div class="band"></div>
  </section>
</main>
</body>
</html>
```